Tovani Nightclub

Nightclub flyer., digital single sided, for FB and IG. I included samples of some previous flyers we've used. Sample Info:
TOVANI
FRIDAYS
FRI MAY 1 2020
DJ BRAVURA (club floor)
DJ ZOLT & DJ RAF (residents on the lounge floor)
4372 Birch Street Sacramento
www.tovanimurcott.com for list/VIP inquiries

Target Market(s)

Upscale top 40 crowd but want some cool and artsy like the examples included.

Font styles to use
Sans Serif

Requirements
Must have
• Tovani Logo
Nice to have
• Would be nice if the flyer can be incorporated later with DJ photos (sometimes we will add dj photos to instagram etc). Would like a big city type of feel.
Should not have
• Nothing too sexual.

```html
<!DOCTYPE html>
<html lang="en">
<head>
<meta charset="utf-8">
<title>Tovani Fridays Flyer</title>
<link rel="stylesheet" href="https://fonts.googleapis.com/css2?family=Anton&family=Bebas+Neue&family=Kaushan+Script&family=Roboto:wght@500;700&display=swap">
<style>
  :root {
    --page-bg: #040b17;
    --violet-top: #3a2f9c;
    --violet-mid: #2c2685;
    --navy-deep: #0c0a26;
    --gold: #dcc04e;
    --gold-soft: #e8d27a;
    --white: #ffffff;
    --ribbon-fill: #2e2878;
    --photo-magenta: #b3206d;
    --photo-violet: #3b2a86;
    --stripe: rgba(120, 110, 220, 0.55);
  }
  * { margin: 0; padding: 0; box-sizing: border-box; }
  html, body {
    width: 1200px;
    height: 1200px;
    overflow: hidden;
    background: var(--page-bg);
  }
  .flyer {
    position: absolute;
    left: 220px;
    top: 63px;
    width: 760px;
    height: 1073px;
    overflow: hidden;
    background: linear-gradient(180deg, var(--violet-top) 0%, var(--violet-mid) 45%, #1f1a5e 70%, var(--navy-deep) 100%);
  }
  .flyer-photo {
    position: absolute;
    left: 78px;
    top: 74px;
    width: 590px;
    height: 380px;
    background:
      radial-gradient(ellipse 42% 55% at 52% 40%, var(--photo-magenta) 0%, rgba(179, 32, 109, 0.45) 45%, rgba(59, 42, 134, 0) 80%),
      linear-gradient(180deg, rgba(59, 42, 134, 0.6), rgba(44, 38, 133, 0));
  }
  .flyer-stripes {
    position: absolute;
    left: 0;
    top: 0;
  }
  .date-ribbon {
    position: absolute;
    left: 571px;
    top: 0;
    width: 117px;
    height: 224px;
  }
  .date-ribbon__text {
    position: absolute;
    left: 0;
    width: 117px;
    text-align: center;
    font-family: "Bebas Neue", sans-serif;
    line-height: 1;
  }
  .date-ribbon__day { top: 28px; font-size: 50px; color: var(--gold); }
  .date-ribbon__month { top: 79px; font-size: 42px; color: var(--white); }
  .date-ribbon__num { top: 120px; font-size: 60px; color: var(--gold); }
  .brand-name {
    position: absolute;
    left: 0;
    width: 760px;
    top: 400px;
    text-align: center;
    font-family: "Anton", sans-serif;
    font-size: 218px;
    line-height: 1;
    letter-spacing: -2px;
    color: var(--gold);
  }
  .night-name {
    position: absolute;
    left: 0;
    width: 760px;
    top: 552px;
    text-align: center;
    font-family: "Kaushan Script", cursive;
    font-size: 128px;
    line-height: 1.1;
    color: var(--white);
  }
  .lineup {
    position: absolute;
    left: 40px;
    width: 720px;
    top: 776px;
    text-align: center;
    color: var(--white);
  }
  .lineup__dj {
    font-family: "Bebas Neue", sans-serif;
    font-size: 54px;
    line-height: 1;
    letter-spacing: 1px;
  }
  .lineup__floor {
    font-family: "Roboto", sans-serif;
    font-weight: 500;
    font-size: 20px;
    line-height: 1.2;
    margin-top: 6px;
    margin-bottom: 22px;
  }
  .venue {
    position: absolute;
    left: 40px;
    width: 720px;
    top: 992px;
    text-align: center;
    font-family: "Roboto", sans-serif;
    font-weight: 700;
  }
  .venue__address {
    font-size: 31px;
    line-height: 1;
    color: var(--gold);
    letter-spacing: 0.5px;
  }
  .venue__web {
    font-size: 18px;
    line-height: 1;
    margin-top: 11px;
    color: var(--white);
  }
</style>
</head>
<body>
  <main class="flyer">
    <div class="flyer-photo" role="img" aria-label="Photo of a DJ with headphones dancing, lit in magenta"></div>

    <svg class="flyer-stripes" width="760" height="1073" viewBox="0 0 760 1073" aria-hidden="true">
      <g stroke="var(--stripe)" stroke-width="10">
        <line x1="560" y1="420" x2="780" y2="260"/>
        <line x1="580" y1="450" x2="780" y2="300"/>
        <line x1="600" y1="480" x2="780" y2="340"/>
        <line x1="620" y1="510" x2="780" y2="380"/>
      </g>
    </svg>

    <svg class="date-ribbon" width="117" height="224" viewBox="0 0 117 224" aria-hidden="true">
      <path d="M2 0 V221 L58.5 190 L115 221 V0" fill="var(--ribbon-fill)" stroke="var(--gold)" stroke-width="4"/>
    </svg>
    <div class="date-ribbon__text date-ribbon__day">FRI</div>
    <div class="date-ribbon__text date-ribbon__month">MAY</div>
    <div class="date-ribbon__text date-ribbon__num">01</div>

    <h1 class="brand-name">TOVANI</h1>
    <div class="night-name">Fridays</div>

    <section class="lineup">
      <div class="lineup__dj">DJ BRAVURA</div>
      <div class="lineup__floor">(club floor)</div>
      <div class="lineup__dj">DJ ZOLT &amp; DJ RAF</div>
      <div class="lineup__floor">(residents on the lounge floor)</div>
    </section>

    <footer class="venue">
      <div class="venue__address">4372 BIRCH STREET SACRAMENTO</div>
      <div class="venue__web">www.tovanimurcott.com for list/VIP inquiries</div>
    </footer>
  </main>
</body>
</html>
```